Bourbon Lantern is a speakeasy whiskey and cigar website needing fresh look for product sales

This is a new company just starting out that will be Design needs to be modern edge of prohibition of the 1920's and the speakeasies that were created from them. Needs to include the moonshine runners, stills and whiskey. Also needs to have the sophistication of a speakeasy where gentlemen and now women go to sit in luxury leather chairs with their whiskey and cigar. Lastly my website will not be selling alcohol or cigars. Just higher end accessories and furniture designs in the Bourbon Lantern store that will help the consumer feel like they are back in time while sitting in the comfort of their own speakeasy.

I will attach my current logo but I am open to suggestions to better suit my vision. I do have photos of products that have been purchased to put on website. I am leaving the designs of actual website itself to the designer.

Target Market(s)

21 yrs +; home owners; mature audience; redesign room; cigar accessories; liquor accessories

Industry/Entity Type

home bars, liquor accessories, cigar accessories

Coding

Coded - Design and coding required

Number of Pages Required

1 page

Font styles to use
Serif
Decorative
Script

Colors

Designer to choose colors to be used in the design.

Requirements
Must have
• key words for search engines, eye catching designs matching key words, links to online store and social media
Nice to have
• logo, mixture of retro/old feel with modern day twist; speakeasy/moonshine runners with luxury and class
Should not have
• nudity, XXX, racism

```html
<!DOCTYPE html>
<html lang="en">
<head>
<meta charset="utf-8">
<title>Bourbon Lantern Store</title>
<link href="https://fonts.googleapis.com/css2?family=Pinyon+Script&family=Raleway:wght@400;600;700&display=swap" rel="stylesheet">
<style>
:root{
  --page:#8f8a86;
  --tan:#b59a82;
  --cream:#ebe6d8;
  --paper:#ffffff;
  --mist:#ededed;
  --ink:#1c1c1c;
  --text:#555;
  --soft:#8a8a8a;
  --black:#0b0b0b;
  --white:#fff;
  --graphite-1:#e6e3de;
  --graphite-2:#cfcbc4;
  --graphite-3:#bdb8b0;
}
*{margin:0;padding:0;box-sizing:border-box}
html,body{width:1200px;height:4204px;overflow:hidden}
body{background:var(--page);font-family:"Raleway",sans-serif;color:var(--text);position:relative}
.site{position:absolute;left:60px;top:60px;width:1080px;height:4080px;background:var(--paper);overflow:hidden}
.abs{position:absolute}
.script{font-family:"Pinyon Script",cursive;font-weight:400;white-space:nowrap}

/* nav */
.nav{left:0;top:0;width:1080px;height:60px;background:var(--tan);font-size:13px;color:var(--white)}
.nav a{position:absolute;top:22px;color:var(--white);text-decoration:none;letter-spacing:.5px}
.brand-badge{left:480px;top:0;width:120px;height:120px;border-radius:50%;background:var(--black);border:3px solid var(--tan);display:flex;align-items:center;justify-content:center;text-align:center;color:var(--white);font-size:13px;font-weight:600;letter-spacing:1px;z-index:3;line-height:1.3}

/* hero */
.hero{left:0;top:60px;width:1080px;height:500px;background:linear-gradient(100deg,#2a1a12 0%,#4a2e1c 45%,#6b4325 70%,#3a2416 100%)}
.hero-shade{left:0;top:60px;width:620px;height:500px;background:linear-gradient(90deg,rgba(0,0,0,.55),rgba(0,0,0,0))}
.hero-title{left:100px;top:260px;font-size:58px;color:var(--white)}
.hero-sub{left:100px;top:352px;font-size:22px;font-weight:700;color:var(--white)}
.hero-copy{left:100px;top:388px;width:430px;font-size:15px;line-height:1.45;color:#eee}

/* about */
.about{left:0;top:560px;width:1080px;height:420px;background:var(--cream)}
.eyebrow{font-size:13px;font-weight:700;letter-spacing:1.5px;color:var(--ink)}
.about .eyebrow{left:120px;top:92px}
.about-title{left:120px;top:110px;font-size:58px;color:var(--ink)}
.about-copy{left:120px;top:200px;width:440px;font-size:13px;line-height:1.75;color:var(--soft)}
.about-photo{left:572px;top:80px;width:496px;height:330px;border:6px solid var(--white);box-shadow:0 4px 14px rgba(0,0,0,.2);background:linear-gradient(120deg,#5a2e1a,#a5623a 55%,#3b2015)}

/* sketch illustration area */
.sketch-band{left:0;top:980px;width:1080px;height:520px;background:
  radial-gradient(ellipse 260px 150px at 560px 250px,var(--graphite-3),rgba(189,184,176,0) 100%),
  radial-gradient(ellipse 220px 170px at 130px 260px,var(--graphite-2),rgba(207,203,196,0) 100%),
  radial-gradient(ellipse 180px 200px at 960px 260px,var(--graphite-2),rgba(207,203,196,0) 100%),
  linear-gradient(180deg,var(--cream) 0%,var(--graphite-1) 14%,#dedad4 55%,#efede9 82%,var(--paper) 100%)}

/* section heads */
.center{left:0;width:1080px;text-align:center}
.sec-eyebrow{font-size:13px;font-weight:700;letter-spacing:1.5px;color:var(--ink)}
.sec-title{font-size:56px;color:var(--ink)}
.sec-copy{left:190px;width:700px;text-align:center;font-size:13px;line-height:1.7;color:var(--soft)}
.rule{height:1px;background:#ccc}

/* services */
.svc-photo{border:6px solid var(--white);box-shadow:0 6px 16px rgba(0,0,0,.25)}
.svc-1{left:-6px;top:1728px;width:686px;height:452px;background:linear-gradient(110deg,#2b170d,#6a3a1d 45%,#b7783a 65%,#3a1e10)}
.svc-2{left:460px;top:2100px;width:572px;height:460px;background:linear-gradient(130deg,#1e130d,#4b2e1b 50%,#8a5a32 70%,#24160e)}
.svc-3{left:80px;top:2428px;width:500px;height:432px;background:linear-gradient(120deg,#2c1a14,#7d2a1e 45%,#b05a3a 60%,#2a1810)}
.svc-head{font-size:15px;font-weight:600;color:var(--ink);letter-spacing:.5px}
.svc-copy{font-size:12px;line-height:1.7;color:var(--soft);width:210px}
.btn{display:inline-block;background:var(--tan);color:var(--white);font-size:11px;font-weight:700;letter-spacing:1px;padding:9px 22px;border-radius:16px}
.sketch-corner{left:740px;top:2660px;width:340px;height:220px;background:
  radial-gradient(ellipse 150px 100px at 230px 130px,var(--graphite-2),rgba(207,203,196,0) 100%),
  linear-gradient(200deg,#f6f5f2,#e9e6e1)}

/* products */
.products{left:0;top:2880px;width:1080px;height:600px;background:var(--mist)}
.prod{position:absolute;top:308px;width:156px}
.prod-img{width:156px;height:156px;background:linear-gradient(140deg,#3a2a20,#8b6a4a 60%,#2a1d15)}
.prod-name{margin-top:16px;font-size:13px;font-weight:700;color:var(--ink)}
.prod-copy{margin-top:4px;font-size:10px;line-height:1.5;color:var(--soft)}
.arrow{position:absolute;top:370px}
.prod-sketch{left:0;top:440px;width:150px;height:160px;background:radial-gradient(ellipse 70px 70px at 70px 90px,var(--graphite-2),rgba(207,203,196,0) 100%)}
.prod-sketch.right{left:900px;width:180px}

/* contact */
.contact{left:0;top:3480px;width:1080px;height:540px;background:var(--black)}
.contact-brand{left:80px;top:70px;width:340px;height:300px;display:flex;align-items:center;justify-content:center;gap:14px;color:#cfcfcf;font-size:26px;font-weight:600;letter-spacing:2px;white-space:nowrap}
.contact-brand .dot{width:22px;height:22px;border-radius:50%;background:#cfcfcf;flex:none}
.socials{left:200px;top:440px;display:flex;gap:16px}
.socials span{width:20px;height:20px;border-radius:50%;background:var(--white);display:block}
.contact-title{left:560px;top:60px;font-size:56px;color:var(--white)}
.contact-copy{left:560px;top:140px;width:440px;font-size:12px;line-height:1.6;color:#999}
.field{position:absolute;left:560px;width:450px;border:1px solid #333;background:#141414;color:#aaa;font-size:11px;padding:10px 12px}
.contact .btn{position:absolute;left:560px;top:440px}

.footer{left:0;top:4020px;width:1080px;height:60px;background:var(--tan);color:var(--white);font-size:11px;text-align:center;line-height:60px}
</style>
</head>
<body>
<div class="site">

  <nav class="nav abs">
    <a style="left:318px">Home</a>
    <a style="left:390px">Services</a>
    <a style="left:636px">Our Products</a>
    <a style="left:740px">Contact Us</a>
  </nav>
  <div class="brand-badge abs">BOURBON<br>LANTERN</div>

  <div class="hero abs" role="img" aria-label="Photo of a candle-lit speakeasy lounge with leather armchairs, wooden shelves of whiskey and guests toasting"></div>
  <div class="hero-shade abs"></div>
  <h1 class="hero-title abs script">Bourbon Lantern Store</h1>
  <p class="hero-sub abs">High End Accessories and Furniture Designs</p>
  <p class="hero-copy abs">Lorem ipsum dolor sit amet, consectetur adipiscing elit, sed do eiusmod tempor incididunt ut labore et dolore</p>

  <section class="about abs">
    <p class="eyebrow abs">ABOUT</p>
    <h2 class="about-title abs script">Bourbon Lantern</h2>
    <p class="about-copy abs">Lorem ipsum dolor sit amet, consectetur adipiscing elit, sed do eiusmod tempor incididunt ut labore et dolore magna aliqua. Quis ipsum suspendisse ultrices gravida. Risus commodo viverra maecenas accumsan lacus vel facilisis. Lorem ipsum dolor sit amet, consectetur adipiscing elit, sed do eiusmod tempor incididunt ut labore et dolore magna aliqua. Quis ipsum suspendisse ultrices gravida. Risus commodo viverra maecenas accumsan lacus vel facilisis.</p>
    <div class="about-photo abs" role="img" aria-label="Photo of friends raising whiskey glasses around a small lounge table"></div>
  </section>

  <div class="sketch-band abs" role="img" aria-label="Pencil sketch of a speakeasy bar with stools, a tufted armchair, a whiskey barrel wagon and scattered bottles"></div>

  <p class="sec-eyebrow abs center" style="top:1500px">OUR</p>
  <h2 class="sec-title abs center script" style="top:1516px">Services</h2>
  <div class="rule abs" style="left:190px;top:1600px;width:700px"></div>
  <p class="sec-copy abs" style="top:1612px">Lorem ipsum dolor sit amet, consectetur adipiscing elit, sed do eiusmod tempor incididunt ut labore et dolore magna aliqua. Quis ipsum suspendisse ultrices gravida. Risus commodo viverra maecenas accumsan lacus.</p>

  <div class="svc-photo svc-1 abs" role="img" aria-label="Photo of a dark wood library bar with leather chairs and lit whiskey shelves"></div>
  <div class="abs" style="left:732px;top:1788px">
    <p class="svc-head">LOREM IPSUM</p>
    <p class="svc-copy" style="margin-top:10px">Lorem ipsum dolor sit amet, consectetur adipiscing elit, sed do eiusmod tempor incididunt ut labore et dolore magna aliqua. Quis ipsum suspendisse ultrices gravida risus commodo.</p>
  </div>

  <div class="svc-photo svc-2 abs" role="img" aria-label="Photo of a warm-lit bar room with backlit panels and tufted leather booths"></div>
  <div class="abs" style="left:92px;top:2210px">
    <p class="svc-head">LOREM IPSUM</p>
    <p class="svc-copy" style="margin-top:10px">Duis aute irure dolor in reprehenderit in voluptate velit esse cillum dolore eu fugiat nulla pariatur excepteur sint.</p>
  </div>

  <div class="sketch-corner abs" role="img" aria-label="Faint pencil sketch of bottles, a glass and a country still house"></div>
  <div class="svc-photo svc-3 abs" role="img" aria-label="Photo of a red velvet armchair and lamp in a dim speakeasy corner"></div>
  <div class="abs" style="left:652px;top:2600px">
    <p class="svc-head">LOREM IPSUM</p>
    <p class="svc-copy" style="margin-top:10px">Lorem ipsum dolor sit amet, consectetur adipiscing elit sed do eiusmod tempor magna aliqua.</p>
    <span class="btn" style="margin-top:16px">LEARN MORE</span>
  </div>

  <section class="products abs">
    <div class="prod-sketch abs" role="img" aria-label="Faint pencil sketch of a whiskey bottle and glass"></div>
    <div class="prod-sketch right abs" role="img" aria-label="Faint pencil sketch of cigar accessories"></div>
    <p class="sec-eyebrow abs center" style="top:38px">OUR</p>
    <h2 class="sec-title abs center script" style="top:54px">Products</h2>
    <div class="rule abs" style="left:190px;top:136px;width:700px"></div>
    <p class="sec-copy abs" style="top:148px">Lorem ipsum dolor sit amet, consectetur adipiscing elit, sed do eiusmod tempor incididunt ut labore et dolore magna aliqua. Quis ipsum suspendisse ultrices gravida. Risus commodo viverra maecenas accumsan lacus vel facilisis.</p>

    <svg class="arrow" style="left:68px" width="16" height="24" viewBox="0 0 16 24"><path d="M12 3 L4 12 L12 21" fill="none" stroke="#333" stroke-width="2.5"/></svg>
    <svg class="arrow" style="left:996px" width="16" height="24" viewBox="0 0 16 24"><path d="M4 3 L12 12 L4 21" fill="none" stroke="#333" stroke-width="2.5"/></svg>

    <div class="prod" style="left:108px">
      <div class="prod-img" role="img" aria-label="Product photo of a brass cigar lighter"></div>
      <p class="prod-name">LOREM IPSUM</p>
      <p class="prod-copy">Sed do eiusmod tempor incididunt ut labore magna.</p>
    </div>
    <div class="prod" style="left:284px">
      <div class="prod-img" role="img" aria-label="Product photo of a leather cigar case"></div>
      <p class="prod-name">MAURIS AUCTOR</p>
      <p class="prod-copy">Quis ipsum suspendisse ultrices gravida risus.</p>
    </div>
    <div class="prod" style="left:460px">
      <div class="prod-img" role="img" aria-label="Product photo of a wooden cigar humidor"></div>
      <p class="prod-name">DONEC FINIBUS</p>
      <p class="prod-copy">Commodo viverra maecenas accumsan lacus vel.</p>
    </div>
    <div class="prod" style="left:636px">
      <div class="prod-img" style="background:linear-gradient(140deg,#1c2230,#6f7f95 55%,#20242c)" role="img" aria-label="Product photo of cut crystal whiskey glasses"></div>
      <p class="prod-name">PHASELLUS</p>
      <p class="prod-copy">Facilisis lorem ipsum dolor sit amet elit.</p>
    </div>
    <div class="prod" style="left:812px">
      <div class="prod-img" role="img" aria-label="Product photo of a whiskey decanter set"></div>
      <p class="prod-name">VIVAMUS</p>
      <p class="prod-copy">Tempor incididunt ut labore dolore magna.</p>
    </div>

    <span class="btn abs" style="left:498px;top:552px">VIEW ALL</span>
  </section>

  <section class="contact abs">
    <div class="contact-brand abs"><span class="dot"></span>BOURBON LANTERN</div>
    <div class="socials abs"><span></span><span></span><span></span></div>
    <h2 class="contact-title abs script">Contact us</h2>
    <p class="contact-copy abs">Lorem ipsum dolor sit amet, consectetur adipiscing elit, sed do eiusmod tempor incididunt ut labore et dolore magna aliqua.</p>
    <div class="field" style="top:212px;height:34px">Full Name</div>
    <div class="field" style="top:256px;height:34px">Your Email Address</div>
    <div class="field" style="top:300px;height:120px">Your Message</div>
    <span class="btn">SUBMIT</span>
  </section>

  <footer class="footer abs">Copyright 2024 bourbonlantern.example All Rights Reserved</footer>
</div>
</body>
</html>
```